Welding Fabrication and Inspection Business Card Design

Welding Fabrication and Inspection Services,

Business

Industrial Machinery ServicesMohammed Rahim30 Ballarat Street, Mount Gravatt East.4122.QLD

```html
<!DOCTYPE html>
<html lang="en">
<head>
<meta charset="utf-8">
<title>Tarnwell Forge Services – Business Card</title>
<link href="https://fonts.googleapis.com/css2?family=Lato:wght@400;700;900&display=swap" rel="stylesheet">
<style>
  :root {
    --page-bg: #e9e7e4;
    --card-white: #ffffff;
    --ink-dark: #1f1f1f;
    --ink-text: #333333;
    --accent-red: #8e1b1b;
    --band-grey: #3a3a3a;
    --rule-grey: #b9b9b9;
  }
  * { margin: 0; padding: 0; box-sizing: border-box; }
  html, body {
    width: 1200px;
    height: 913px;
    overflow: hidden;
    background: var(--page-bg);
    font-family: "Lato", Arial, sans-serif;
  }
  .stage {
    width: 1200px;
    height: 913px;
    display: flex;
    align-items: center;
    justify-content: center;
  }
  .business-card {
    position: relative;
    width: 760px;
    height: 434px;
    background: var(--card-white);
    box-shadow: 0 10px 30px rgba(0,0,0,0.18);
    display: flex;
    flex-direction: column;
    align-items: center;
    overflow: hidden;
  }
  .brand {
    margin-top: 96px;
    display: flex;
    align-items: center;
    gap: 12px;
  }
  .brand-dot {
    width: 14px;
    height: 14px;
    border-radius: 50%;
    background: var(--ink-dark);
  }
  .brand-name {
    font-weight: 900;
    font-size: 30px;
    color: var(--ink-dark);
    letter-spacing: 0.3px;
  }
  .person-name {
    margin-top: 54px;
    font-weight: 700;
    font-size: 22px;
    color: var(--accent-red);
    text-transform: uppercase;
    letter-spacing: 1.5px;
  }
  .name-rule {
    margin-top: 10px;
    width: 150px;
    height: 1px;
    background: linear-gradient(to right, transparent, var(--rule-grey), transparent);
  }
  .address {
    margin-top: 26px;
    font-size: 17px;
    color: var(--ink-text);
    letter-spacing: 0.3px;
  }
  .footer-band {
    position: absolute;
    left: 0;
    right: 0;
    bottom: 8px;
    height: 20px;
    background: var(--band-grey);
  }
  .footer-edge {
    position: absolute;
    left: 0;
    right: 0;
    bottom: 0;
    height: 4px;
    background: var(--band-grey);
  }
</style>
</head>
<body>
  <main class="stage">
    <section class="business-card">
      <div class="brand">
        <span class="brand-dot"></span>
        <span class="brand-name">Tarnwell Forge Services</span>
      </div>
      <p class="person-name">Khalid Nasser</p>
      <div class="name-rule"></div>
      <p class="address">17 Corrowen Street, Mount Harrow East. 4190.QLD</p>
      <div class="footer-band"></div>
      <div class="footer-edge"></div>
    </section>
  </main>
</body>
</html>
```